Law Office Business Card

We need a business card design to include the following information:
Name of Firm: Brennick Law Group, P.A.
Address: 4627 Sandlot Ave, Ste 208, West Palm Beach, FL 33409
Phone: 561-555-0148
Fax: 561-555-0193
Website: http://www.tbrennicklaw.example

We Need a place for the Person's name and email address. Please start with the following:
Lorna K. Dwyer, Esq.
lorna@tbrennicklaw.example

```html
<!DOCTYPE html>
<html lang="en">
<head>
<meta charset="utf-8">
<title>Brennick Law Group – Business Card</title>
<link rel="stylesheet" href="https://fonts.googleapis.com/css2?family=Source+Sans+3:wght@400;600&display=swap">
<style>
  :root {
    --stage: #000000;
    --card: #35363a;
    --gold: #bfae93;
    --ink: #ffffff;
    --rule: #a99c87;
  }
  * { margin: 0; padding: 0; box-sizing: border-box; }
  html, body {
    width: 1200px; height: 900px; overflow: hidden;
    background: var(--stage);
    font-family: "Source Sans 3", "Myriad Pro", Arial, sans-serif;
  }
  .stage { position: relative; width: 1200px; height: 900px; }
  .card {
    position: absolute; top: 271px;
    width: 457px; height: 281px;
    background: var(--card);
    border-radius: 14px;
    overflow: hidden;
  }
  .card--contact { left: 137px; }
  .card--brand { left: 626px; }
  .card-frame { position: absolute; inset: 0; width: 100%; height: 100%; }
  .card-frame path { fill: none; stroke: var(--rule); stroke-width: 1.3; }

  .contact { position: absolute; left: 0; right: 0; text-align: center; color: var(--ink); font-size: 13px; line-height: 18.5px; }
  .contact .label { color: var(--gold); font-weight: 600; }
  .person { top: 48px; }
  .person-name { color: var(--gold); font-weight: 600; font-size: 17px; line-height: 22px; }
  .lines { top: 110px; }
  .firm { top: 187px; }
  .firm-name { color: var(--gold); font-weight: 600; font-size: 13.5px; }

  .brand {
    position: absolute; left: 0; right: 0; top: 155px;
    display: flex; align-items: center; justify-content: center; gap: 12px;
  }
  .brand-mark { width: 14px; height: 14px; background: var(--gold); }
  .brand-name {
    color: var(--gold); font-weight: 400; font-size: 26px; letter-spacing: 0.5px;
  }
</style>
</head>
<body>
<main class="stage">
  <section class="card card--contact">
    <svg class="card-frame" viewBox="0 0 457 281" aria-hidden="true">
      <path d="M361 22 H422 V72"/>
      <path d="M34 196 V246 H96"/>
    </svg>
    <div class="contact person">
      <p class="person-name">Lorna K. Dwyer, Esq.</p>
      <p>lorna@tbrennicklaw.example</p>
    </div>
    <div class="contact lines">
      <p><span class="label">T:</span> 561-555-0148</p>
      <p><span class="label">F:</span> 561-555-0193</p>
      <p><span class="label">W:</span> www.tbrennicklaw.example</p>
    </div>
    <div class="contact firm">
      <p class="firm-name">Brennick Law Group, P.A.</p>
      <p>4627 Sandlot Ave, Ste 208, West Palm Beach, FL 33409</p>
    </div>
  </section>

  <section class="card card--brand">
    <svg class="card-frame" viewBox="0 0 457 281" aria-hidden="true">
      <path d="M100 29 H38 V79"/>
      <path d="M427 203 V252 H366"/>
    </svg>
    <div class="brand">
      <span class="brand-mark"></span>
      <span class="brand-name">Brennick Law Group</span>
    </div>
  </section>
</main>
</body>
</html>
```